Lectres app for Android

We need design for Android application for selling audio lectures. The author of the lectures is a fairly well-known philologist and writer who has lectured on various topics (film, literature, etc.)

Design for the same iOS app has been succesfuly developed about nine month ago.

Design have to be developed for both tablet and phone in the "Matherial design" style and with colours as at existing app (see attachments).

There are 5 screens in this application.

1. Splash screen with application title "Vurda's library". This screen appears for 2-3 seconds at the app start.

2. Screen with a list of lectures. There must be the Author's photo (logo) and the app title in the screen as well as the list of lectures (starting from the last one) with pictures. The sketch in the attachment. Each lecture must have a category mark (movies, literature) as well as the title and a short description. In the list must be some difference between fully listened to lectures, thouse that haven't been listened to to the end. And thouse haven't been purchased yet. In the attached layout it is marked with the color of the ring next to each item. We need small palaying status at the bottom of the screen In the phone design (see attachment).
3. Player screen..It is desirable to see the progress of the lectures, title, lectures picture^ an opportunity to download it for listening offline, an icon to mark the lecture as the listened to, total duration and current position. .

4. Purchase screen

5. Info screen with some app settings (restore purchase, entering promo code and change a language).

The design should be in the "Material design" style and with colours as in the iOS app.

See existing iOS design in the files iOS4-iOS4.png

```html
<!DOCTYPE html>
<html lang="en">
<head>
<meta charset="utf-8">
<title>Now Playing — Vurda's library</title>
<link rel="stylesheet" href="https://fonts.googleapis.com/css2?family=Roboto:wght@300;400;500&display=swap">
<style>
  :root {
    --status-orange: #e9511d;
    --bar-orange: #ff5722;
    --accent-orange: #f26b3a;
    --badge-green: #8bc34a;
    --white: #ffffff;
    --ink: #333333;
    --track-grey: #555555;
    --cover-top: #d8d2bc;
    --cover-mid: #b4ccc5;
    --cover-bottom: #9fa593;
  }
  * { margin: 0; padding: 0; box-sizing: border-box; }
  html, body {
    width: 675px; height: 1200px; overflow: hidden;
    background: var(--white);
    font-family: "Roboto", Arial, sans-serif;
  }
  .screen { position: relative; width: 675px; height: 1200px; overflow: hidden; }

  .status-bar {
    position: absolute; left: 0; top: 0; width: 675px; height: 45px;
    background: var(--status-orange); color: var(--white);
  }
  .status-bar svg { position: absolute; left: 524px; top: 11px; }
  .status-time { position: absolute; right: 17px; top: 9px; font-size: 24px; font-weight: 400; }

  .app-bar {
    position: absolute; left: 0; top: 45px; width: 675px; height: 105px;
    background: var(--bar-orange); color: var(--white);
  }
  .menu-icon { position: absolute; left: 35px; top: 38px; }
  .app-title {
    position: absolute; left: 119px; top: 25px;
    font-size: 35px; font-weight: 400; letter-spacing: 0.2px;
  }
  .cart-icon { position: absolute; left: 562px; top: 26px; }
  .more-icon { position: absolute; left: 624px; top: 32px; }

  .cover {
    position: absolute; left: 0; top: 150px; width: 675px; height: 935px;
    background: linear-gradient(180deg, var(--cover-top) 0%, var(--cover-mid) 45%, var(--cover-bottom) 100%);
  }
  .cover-title {
    position: absolute; left: 0; top: 150px; width: 675px; height: 935px;
    display: flex; flex-direction: column; justify-content: center; align-items: center;
    color: var(--white); font-weight: 300; font-size: 48px; line-height: 55px;
    letter-spacing: 0.5px; text-transform: uppercase; text-align: center; padding-bottom: 8px;
  }

  .player-bar {
    position: absolute; left: 0; top: 1085px; width: 675px; height: 115px;
    background: var(--white);
  }
  .pause-button { position: absolute; left: 22px; top: 37px; }
  .track-title {
    position: absolute; left: 0; width: 675px; top: 10px; text-align: center;
    font-size: 15px; color: var(--ink);
  }
  .track-author {
    position: absolute; left: 0; width: 675px; top: 32px; text-align: center;
    font-size: 11px; color: var(--accent-orange);
  }
  .track-category {
    position: absolute; left: 0; width: 675px; top: 76px; text-align: center;
    font-size: 11px; color: var(--accent-orange);
  }
  .time-left { position: absolute; left: 79px; top: 48px; font-size: 15px; color: var(--ink); }
  .time-total { position: absolute; left: 545px; top: 48px; font-size: 15px; color: var(--accent-orange); }
  .progress {
    position: absolute; left: 141px; top: 51px; width: 382px; height: 15px;
    border-radius: 8px; background: var(--track-grey); overflow: hidden;
  }
  .progress-fill { position: absolute; left: 0; top: 0; width: 313px; height: 15px; background: var(--bar-orange); }
  .progress-thumb { position: absolute; left: 313px; top: 0; width: 8px; height: 15px; background: var(--white); }
  .download-button { position: absolute; left: 614px; top: 40px; }
</style>
</head>
<body>
<main class="screen">
  <div class="status-bar">
    <svg width="100" height="24" viewBox="0 0 100 24" aria-hidden="true">
      <polygon points="0,22 22,22 22,0" fill="#ffffff" opacity="0.85"/>
      <rect x="41" y="0" width="14" height="23" rx="2" fill="#ffffff" opacity="0.5"/>
      <rect x="41" y="9" width="14" height="14" rx="2" fill="#ffffff"/>
    </svg>
    <span class="status-time">12:30</span>
  </div>

  <header class="app-bar">
    <svg class="menu-icon" width="34" height="24" viewBox="0 0 34 24" aria-label="Menu" role="img">
      <rect x="0" y="0" width="34" height="3.5" fill="#ffffff"/>
      <rect x="0" y="10" width="34" height="3.5" fill="#ffffff"/>
      <rect x="0" y="20" width="34" height="3.5" fill="#ffffff"/>
    </svg>
    <h1 class="app-title">Now Playing</h1>
    <svg class="cart-icon" width="42" height="44" viewBox="0 0 42 44" aria-label="Cart, 2 items" role="img">
      <path d="M10 16 V12 a8 8 0 0 1 16 0 V16" fill="none" stroke="#ffffff" stroke-width="3"/>
      <path d="M4 16 H32 V40 a2 2 0 0 1 -2 2 H6 a2 2 0 0 1 -2 -2 Z" fill="#ffffff"/>
      <circle cx="29" cy="13" r="10" fill="var(--badge-green)"/>
      <text x="29" y="18" text-anchor="middle" font-family="Roboto, Arial, sans-serif" font-size="14" font-weight="500" fill="#ffffff">2</text>
    </svg>
    <svg class="more-icon" width="14" height="36" viewBox="0 0 14 36" aria-label="More options" role="img">
      <circle cx="7" cy="4" r="3.8" fill="#ffffff"/>
      <circle cx="7" cy="17" r="3.8" fill="#ffffff"/>
      <circle cx="7" cy="30" r="3.8" fill="#ffffff"/>
    </svg>
  </header>

  <div class="cover" role="img" aria-label="Lecture cover photo: meadow grass in soft morning light"></div>
  <h2 class="cover-title"><span>Philosophy of Love</span><span>in the Western World</span></h2>

  <footer class="player-bar">
    <svg class="pause-button" width="34" height="43" viewBox="0 0 34 43" aria-label="Pause" role="img">
      <rect x="0" y="0" width="11" height="43" rx="3" fill="#444444"/>
      <rect x="23" y="0" width="11" height="43" rx="3" fill="#444444"/>
    </svg>
    <p class="track-title">Philosophy of Love in the Western World</p>
    <p class="track-author">by Mara Velick</p>
    <span class="time-left">-59:58</span>
    <div class="progress" role="progressbar" aria-valuenow="82" aria-valuemin="0" aria-valuemax="100">
      <div class="progress-fill"></div>
      <div class="progress-thumb"></div>
    </div>
    <span class="time-total">35:02</span>
    <p class="track-category">Lectures | Philosophy</p>
    <svg class="download-button" width="40" height="38" viewBox="0 0 40 38" aria-label="Download" role="img">
      <rect x="14" y="0" width="12" height="14" fill="var(--bar-orange)"/>
      <polygon points="5,13 35,13 20,28" fill="var(--bar-orange)"/>
      <rect x="1" y="33" width="38" height="4" fill="var(--bar-orange)"/>
    </svg>
  </footer>
</main>
</body>
</html>
```